Chicago Property Management Flyer

We need a brochure/flyer to market our property management services to Chicago property owners. I believe that my preference is single page, double sided, but a bi-fold or tri-fold format may also work. I have provided our logo, and some example images in case that is helpful. Refer to our website at http://www.velmorehq.net/ for more info.

Industry/Entity Type

Property Management

Font styles to use
Sans Serif

```html
<!DOCTYPE html>
<html lang="en">
<head>
<meta charset="utf-8">
<title>Velmore Property Management Flyer</title>
<link href="https://fonts.googleapis.com/css2?family=Fira+Sans+Condensed:wght@500;600;700&display=swap" rel="stylesheet">
<style>
  :root {
    --navy: #1d5482;
    --navy-text: #1f5587;
    --band: #5f6b72;
    --ink: #141414;
    --muted: #5d6368;
    --paper: #ffffff;
  }
  * { margin: 0; padding: 0; box-sizing: border-box; }
  html, body { width: 1200px; height: 1200px; overflow: hidden; background: var(--paper); }
  body { font-family: "Fira Sans Condensed", sans-serif; color: var(--ink); position: relative; }
  .flyer { position: absolute; left: 209px; top: 59px; width: 781px; height: 1106px; }

  .header { position: absolute; left: 9px; top: 0; width: 772px; height: 239px; overflow: hidden; }
  .header-bg { position: absolute; inset: 0; background: linear-gradient(180deg, #d4d6d8 0%, #e6e7e8 45%, #cfd1d3 100%); }
  .brand { position: absolute; left: 30px; top: 166px; display: flex; align-items: center; gap: 10px; }
  .brand-mark { width: 22px; height: 22px; background: var(--navy); }
  .brand-name { font-size: 22px; font-weight: 700; color: var(--navy-text); letter-spacing: 0.3px; }
  .contact { position: absolute; right: 20px; top: 82px; text-align: right; }
  .contact .address { font-size: 17.5px; font-weight: 700; color: var(--navy-text); line-height: 20.5px; }
  .contact .web { font-size: 17px; font-weight: 700; color: var(--muted); margin-top: 21px; line-height: 20px; }
  .contact .email { font-size: 17px; font-weight: 700; color: var(--muted); margin-top: 20px; line-height: 20px; }

  .hero { position: absolute; left: 0; top: 239px; width: 781px; height: 388px; overflow: hidden; }
  .hero-photo { position: absolute; inset: 0; background: linear-gradient(180deg, #c9d3da 0%, #d9dcd8 30%, #8f8f8c 55%, #7a6d62 75%, #6d6a5a 100%); }
  .hero-triangle { position: absolute; inset: 0; }
  .hero-title { position: absolute; right: 11px; top: 190px; text-align: right; color: #fff; font-size: 29px; font-weight: 700; line-height: 47px; }

  .tagline-band { position: absolute; left: 0; top: 627px; width: 781px; height: 69px; background: var(--band); color: #fff; text-align: right; padding: 8px 11px 0 0; font-size: 19px; font-weight: 600; line-height: 31px; }

  .details { position: absolute; left: 0; top: 696px; width: 781px; height: 410px; overflow: hidden; }
  .details-bg { position: absolute; inset: 0; background: linear-gradient(160deg, #eef0ef 0%, #e8e3d8 40%, #e4e6df 70%, #dfe6d9 100%); }
  .benefits { position: absolute; left: 7px; top: 7px; width: 390px; font-size: 10px; font-weight: 600; line-height: 18.4px; }
  .benefits h3, .more h3 { color: var(--navy-text); font-weight: 600; }
  .benefits h3 { font-size: 10px; }
  .more { position: absolute; left: 404px; top: 7px; width: 376px; font-size: 8px; font-weight: 600; line-height: 13.2px; }
  .more h2 { font-size: 12.5px; color: var(--navy-text); font-weight: 700; line-height: 16px; }
  .more .label { color: var(--navy-text); }
  .more p { margin: 0; }
</style>
</head>
<body>
<main class="flyer">
  <header class="header">
    <div class="header-bg" role="img" aria-label="Faded aerial view of the downtown skyline"></div>
    <div class="brand">
      <span class="brand-mark"></span>
      <span class="brand-name">Velmore Property Management</span>
    </div>
    <address class="contact" style="font-style:normal">
      <div class="address">1180 W. Harlow St<br>Chicago IL 60612<br>773-555-0148</div>
      <div class="web">www.velmorehq.net</div>
      <div class="email">dana@velmorehq.net</div>
    </address>
  </header>

  <section class="hero">
    <div class="hero-photo" role="img" aria-label="Chicago skyline seen over neighbourhood rooftops and rail tracks"></div>
    <svg class="hero-triangle" width="781" height="388" viewBox="0 0 781 388">
      <polygon points="423,388 781,0 781,388" fill="#1d5482"/>
    </svg>
    <h1 class="hero-title">Velmore<br>Property<br>Management</h1>
  </section>

  <div class="tagline-band">
    <div>• Managing CHA / Section 8 rentals across Chicago for over a decade.</div>
    <div>• Leverage our experience and expertise to succeed with your properties.</div>
  </div>

  <section class="details">
    <div class="details-bg" role="img" aria-label="Faded view of a brick apartment building with trees"></div>
    <div class="benefits">
      <h3>Save Time and Headaches</h3>
      <p>We have a team in place to tackle all aspects of property management for you.</p>
      <p>Never worry about leasing, tenants, maintenance, regulations, etc.</p>
      <h3>Maximize Your Investment Assets</h3>
      <p>Your properties are expensive assets with lots of potential.</p>
      <p>Put the right professionals in place to protect, maintain, and maximize their value.</p>
      <h3>Increase Income</h3>
      <p>With our experience and market knowledge we can establish optimal rent prices,<br>&nbsp;lease apartments quickly, reduce turnover, and navigate complex housing agency<br>&nbsp;processes to ensure maximum income to you.</p>
      <h3>Reduce Expenses, Maximize Profits</h3>
      <p>Maximize your profits by benefitting from our economies of scale, systems and<br>processes, specialized knowledge, industry network, and buying power</p>
      <h3>Stay Informed</h3>
      <p>With access to all of your property information, documentation, and financials<br>through your online portal of our property management system you and your<br>accountant can stay informed as needed</p>
      <h3>Grow Your Investment Portfolio</h3>
      <p>With our management team focused on profitably managing your existing properties,<br>we can then help you expand to future investments</p>
    </div>
    <div class="more">
      <h2>Additional Content if Needed:</h2>
      <p>Experience We have been managing properties across Chicago for over a decade.<br>&nbsp;Both as direct investors like yourself, and as professional management service<br>&nbsp;provider for local and out-of-state investor clients.</p>
      <p>&nbsp;<span class="label">• Economies of Scale</span>– The large number of properties under our management<br>allow us to gain excellent economies of scale, allowing you efficiency and cost<br>savings as compared to you managing on your own.</p>
      <p>&nbsp;<span class="label">• Systems and Processes</span>– We have developed and implemented the systems<br>and processes to ensure that all aspects of management of your property<br>&nbsp;operate smoothly and efficiently. We utilize integrated management<br>software that allows us to keep information secure and organized, and<br>to stay coordinated with owners, tenants, and maintenance staff.</p>
      <p>&nbsp;<span class="label">• Specialized Knowledge</span>– We already have extensive experience, but still<br>&nbsp;constantly work at improving our property management knowledge and<br>&nbsp;processes. We know what to expect from building and tenant management.<br>We know what works and what does not in today's market.</p>
      <p>&nbsp;<span class="label">• Buying Power</span>– We have worked with numerous contractors and<br>vendors throughout years in property management and performing<br>apartment renovation projects. Our network of resources and volume<br>of work helps to bring the most competitive prices with outside contractors.</p>
      <p>&nbsp;<span class="label">• Network</span> – Our network of vendors and contractors means that we often know the right<br>&nbsp;people to work with for particular jobs if the scope is outside of our<br>standard in-house services.</p>
      <p>&nbsp;<span class="label">• Housing Agency Experts</span> - We are very experienced working with housing agencies such as<br>&nbsp;Chicago Housing Agency Housing Choice Voucher program (formerly known as Section 8).<br>Programs such as this can secure you steady rental income through government funded<br>programs, but can be challenging to navigate the administrative systems, processes,<br>paperwork, and inspections. We can ensure your properties can succeed<br>by working as efficiently as possible through these programs.</p>
    </div>
  </section>
</main>
</body>
</html>
```